Cards & Invitations

Hi!
We would like you to design 3 amazing cards for us.
1. Wedding invitation.
We would like to have a spring wedding invitation. It has to be A4 folded to A5 format, floral theme, but made in a very classic style. It has to contain light green and blue colors, but you are free to use other colors as well.
Text to be included:
Mr. and Mrs. Dwight Vellacombe
Request the honour of your presence
At the marriage of their daughter
Marisa Vellacombe
to
Oscar Lindquay
Saturday, the eighteenth of April
Two thousand and twelve
At three o'clock in the afternoon
Holy Meadow Church
57 Orrin Lane,
South Hampton, New York
Followed by a dinner at
Restaurant Lumiere, Vesey Lane 408
R.S.V.P. by the ninth of April
2. Christening invitation in Vintage style.
We need an invitation for a christening of Nico Darrowby. We would like it to be in vintage style, in light pink or lilac color and containing the photo of the baby.
It should also have some church symbols, like cross, prayer beads etc (one element is enough, not all together). Format: A5 horisontal (landscape) card. Please, find the photo attached.
Text to be included:
You are invited to
Witness and Celebrate
the Baptism of our daughter
Nico Darrowby
Sunday, September 26th at 1 p.m.
Gr. Hollins Church
8871 Tamsin Drive, Parktown
Reception following the ceremony
at the Darrowby home
2093 Whitlow, Pearl Sound
Please reply by September 18th
3. Birthday invitation.
This is an invitation for Nico's 7th birthday party. The theme is racing. It should contain his photo and a race car (cars) or racing competition. No color preferences. It's a square folded card. Please, find attached the photo.
Text on the outside: Nico is turning 7
Text on the inside:
You are invited to join us
for Nico's 7th Birthday Celebration
Saturday, September 18th
We will have the celebration at Blue Otter,
690 Quillan Road, Tamsin Drive
Please reply by September 7th
to Ned at 907-581-362
Welcome!

```html
<!DOCTYPE html>
<html lang="en">
<head>
<meta charset="utf-8">
<title>Spring Wedding Invitation Set</title>
<link rel="stylesheet" href="https://fonts.googleapis.com/css2?family=Pinyon+Script&family=Goudy+Bookletter+1911&family=Crimson+Text&display=swap">
<style>
  :root {
    --backdrop-light: #cfb27f;
    --backdrop-dark: #b8955c;
    --envelope-blue: #03a8e0;
    --envelope-edge: #0391c3;
    --paper: #fdf3f3;
    --label-white: #ffffff;
    --ink-blue: #1ba3d8;
    --ink-green: #7bab1e;
    --ink-black: #111111;
    --card-shadow: 0 4px 10px rgba(0,0,0,0.35);
  }
  * { margin: 0; padding: 0; box-sizing: border-box; }
  html, body { width: 1200px; height: 1080px; overflow: hidden; }
  body {
    position: relative;
    background: radial-gradient(ellipse at 50% 45%, var(--backdrop-light), var(--backdrop-dark));
    font-family: "Goudy Bookletter 1911", Georgia, serif;
  }
  .piece { position: absolute; }
  .section-label {
    position: absolute;
    font-family: "Crimson Text", Georgia, serif;
    font-size: 58px;
    line-height: 1;
    color: var(--ink-black);
  }
  .section-label--inside { left: 786px; top: 82px; }
  .section-label--back { left: 1048px; top: 252px; }
  .section-label--front { left: 38px; top: 474px; }

  .envelope { background: var(--envelope-blue); box-shadow: var(--card-shadow); }
  .envelope--large { left: 41px; top: 20px; width: 720px; height: 448px; }
  .envelope--large .envelope__flap {
    position: absolute; left: 0; top: 0; width: 100%; height: 62px;
    border-bottom: 2px solid var(--envelope-edge);
    border-radius: 0 0 12px 0;
    box-shadow: 0 3px 4px rgba(0,0,0,0.18);
  }
  .envelope--small { left: 882px; top: 820px; width: 294px; height: 236px; }
  .envelope--small svg { position: absolute; left: 0; top: 0; }

  .card { background: var(--paper); box-shadow: var(--card-shadow); overflow: hidden; }
  .card--back { left: 823px; top: 311px; width: 360px; height: 529px; }
  .card--inside { left: 253px; top: 136px; width: 720px; height: 530px; }
  .card--front { left: 40px; top: 531px; width: 360px; height: 531px; }
  .card--rsvp { left: 438px; top: 762px; width: 444px; height: 294px; }

  .floral-art { position: absolute; }
  .card--inside .floral-art {
    left: 5px; top: 134px; width: 342px; height: 396px;
    background: radial-gradient(ellipse at 35% 60%, rgba(132,185,42,0.55), rgba(179,18,46,0.25) 55%, rgba(253,243,243,0) 75%);
  }
  .card--front .floral-art {
    inset: 0;
    background: linear-gradient(160deg, rgba(179,18,46,0.25), rgba(132,185,42,0.35) 45%, rgba(179,18,46,0.3) 80%, rgba(132,185,42,0.3));
  }
  .card--rsvp .floral-art {
    right: 0; bottom: 0; width: 120px; height: 130px;
    background: radial-gradient(ellipse at 70% 70%, rgba(179,18,46,0.45), rgba(132,185,42,0.25) 55%, rgba(253,243,243,0) 75%);
  }

  .script { font-family: "Pinyon Script", cursive; font-weight: 400; }
  .line { position: absolute; white-space: nowrap; }

  .invitation-host { font-size: 16px; color: var(--ink-blue); line-height: 1.2; }
  .host-1 { left: 392px; top: 40px; }
  .host-2 { left: 450px; top: 61px; }
  .host-3 { left: 422px; top: 82px; }

  .couple-line {
    position: absolute; width: 400px; text-align: center;
    color: var(--ink-green); font-size: 48px; line-height: 1; white-space: nowrap;
  }
  .couple-line--bride { left: 329px; top: 146px; }
  .couple-line--to { left: 353px; top: 198px; font-size: 40px; }
  .couple-line--groom { left: 365px; top: 246px; }

  .event-details {
    position: absolute; left: 347px; top: 320px; width: 400px;
    color: var(--ink-blue); font-size: 16px; line-height: 21px; text-align: center;
  }

  .back-title {
    position: absolute; color: var(--ink-blue); font-size: 52px; line-height: 1; white-space: nowrap;
  }
  .back-title--1 { left: 24px; top: 392px; }
  .back-title--2 { left: 158px; top: 438px; font-size: 38px; }
  .back-title--3 { left: 222px; top: 446px; }

  .name-label {
    position: absolute; left: 77px; top: 101px; width: 283px; height: 238px;
    background: var(--label-white);
    border-radius: 8px 0 0 8px;
    box-shadow: -6px 8px 18px rgba(0,0,0,0.4);
    display: flex; flex-direction: column; align-items: center; justify-content: center;
    color: var(--ink-blue); font-size: 36px; line-height: 1.35; text-align: center;
  }

  .rsvp-title {
    position: absolute; left: 0; top: 14px; width: 100%;
    text-align: center; color: var(--ink-green); font-size: 52px; line-height: 1;
  }
  .rsvp-text { color: var(--ink-green); font-size: 17px; }
  .rsvp-name { left: 18px; top: 94px; }
  .rsvp-option { left: 88px; font-variant: small-caps; font-size: 15px; display: flex; align-items: center; }
  .rsvp-option--accept { top: 136px; }
  .rsvp-option--decline { top: 188px; }
  .rsvp-option .tick-circle {
    width: 24px; height: 24px; border: 1.5px solid var(--ink-green); border-radius: 50%;
    margin-right: 10px; flex: none;
  }
  .rsvp-count { left: 130px; top: 161px; font-variant: small-caps; font-size: 13px; }
  .rsvp-deadline { left: 18px; top: 232px; font-variant: small-caps; font-size: 17px; }
</style>
</head>
<body>

  <div class="piece envelope envelope--large"><div class="envelope__flap"></div></div>
  <div class="section-label section-label--inside">inside</div>

  <div class="piece envelope envelope--small">
    <svg width="294" height="236" viewBox="0 0 294 236" aria-hidden="true">
      <path d="M0 20 L130 120 Q147 132 164 120 L294 20" fill="none" stroke="#0391c3" stroke-width="2"/>
    </svg>
  </div>

  <div class="section-label section-label--back">back</div>
  <section class="piece card card--back" aria-label="Invitation back">
    <div class="back-title back-title--1 script">Directions</div>
    <div class="back-title back-title--2 script">and</div>
    <div class="back-title back-title--3 script">Map</div>
  </section>

  <section class="piece card card--inside" aria-label="Invitation inside">
    <div class="floral-art" role="img" aria-label="Red tulip blossoms on curling green stems"></div>
    <div class="line invitation-host host-1">Mr. and Mrs. Dwight Vellacombe</div>
    <div class="line invitation-host host-2">Request the honour of your presence</div>
    <div class="line invitation-host host-3">At the marriage of their daughter</div>
    <h1 class="script">
      <span class="couple-line couple-line--bride">Marisa Vellacombe</span>
      <span class="couple-line couple-line--to">to</span>
      <span class="couple-line couple-line--groom">Oscar Lindquay</span>
    </h1>
    <p class="event-details">
      Saturday, the eighteenth of April<br>
      Two thousand and twelve<br>
      At three o'clock in the afternoon<br>
      Holy Meadow Church<br>
      57 Orrin Lane,<br>
      South Hampton, New York<br>
      Followed by a dinner at<br>
      Restaurant Lumiere, Vesey Lane 408
    </p>
  </section>

  <div class="section-label section-label--front">Front</div>
  <section class="piece card card--front" aria-label="Invitation front">
    <div class="floral-art" role="img" aria-label="Pale tulip and green leaf pattern covering the cover"></div>
    <div class="name-label script">
      <span>Marisa Vellacombe</span>
      <span>Weds</span>
      <span>Oscar Lindquay</span>
    </div>
  </section>

  <section class="piece card card--rsvp" aria-label="Reply card">
    <div class="floral-art" role="img" aria-label="Small red tulips on green stems"></div>
    <div class="rsvp-title script">R.S.V.P.</div>
    <div class="line rsvp-text rsvp-name">Mr/Ms.............................................................</div>
    <div class="line rsvp-text rsvp-option rsvp-option--accept"><span class="tick-circle"></span>accepts with pleasure</div>
    <div class="line rsvp-text rsvp-count">no. attending.....................</div>
    <div class="line rsvp-text rsvp-option rsvp-option--decline"><span class="tick-circle"></span>declines with regret</div>
    <div class="line rsvp-text rsvp-deadline">Your reply is requested by Ninth of April, 2012</div>
  </section>

</body>
</html>
```